Halvex Consulting

Hi,
I have my own network consulting business (just me)
and need to get a logo and business card design together,

Based in New Zealand,

Gareth Pollard
Unified Communications and Network Architect

/design engineer,
and would like this to be the basis for personal branding and company identity

Reason: I will be off site for a couple of days - so you have some more time

Business

• I have the basis for a optional logo - needs color -

```html
<!DOCTYPE html>
<html lang="en">
<head>
<meta charset="utf-8">
<title>Halvex Consulting – Business Card</title>
<link rel="stylesheet" href="https://fonts.googleapis.com/css2?family=Exo+2:wght@700&family=Open+Sans:wght@400&display=swap">
<style>
  :root {
    --page-bg: #ffffff;
    --card-center: #2a8ef0;
    --card-mid: #1565c8;
    --card-edge: #0b3f8e;
    --accent-red: #e3202c;
    --text-white: #ffffff;
    --text-soft: #e6f0ff;
    --divider: #dbe8ff;
    --mark-faint: rgba(90, 170, 255, 0.28);
  }
  html, body {
    margin: 0;
    padding: 0;
    width: 1028px;
    height: 1200px;
    overflow: hidden;
    background: var(--page-bg);
  }
  .canvas {
    position: relative;
    width: 1028px;
    height: 1200px;
  }
  .card {
    position: absolute;
    left: 0;
    width: 1028px;
    height: 570px;
    border-radius: 62px;
    overflow: hidden;
  }
  .card--front {
    top: 0;
    background: radial-gradient(ellipse 60% 70% at 50% 38%, var(--card-center) 0%, var(--card-mid) 45%, var(--card-edge) 100%);
  }
  .card--back {
    top: 628px;
    background: radial-gradient(ellipse 55% 65% at 48% 35%, var(--card-center) 0%, var(--card-mid) 45%, var(--card-edge) 100%);
  }
  .brand {
    position: absolute;
    left: 0;
    right: 0;
    top: 390px;
    display: flex;
    align-items: center;
    justify-content: center;
    gap: 22px;
  }
  .brand__dot {
    width: 46px;
    height: 46px;
    border-radius: 50%;
    background: var(--accent-red);
  }
  .brand__name {
    font-family: "Exo 2", sans-serif;
    font-weight: 700;
    font-size: 54px;
    color: var(--text-white);
    letter-spacing: 0.5px;
  }
  .back-mark {
    position: absolute;
    left: 330px;
    top: 60px;
    width: 300px;
    height: 300px;
    border-radius: 50%;
    background: var(--mark-faint);
  }
  .person {
    position: absolute;
    left: 150px;
    top: 934px;
    font-family: "Open Sans", sans-serif;
    color: var(--text-white);
  }
  .person__name {
    margin: 0 0 14px;
    font-size: 47px;
    font-weight: 400;
    line-height: 60px;
  }
  .person__role {
    margin: 0;
    font-size: 24px;
    line-height: 35px;
    color: var(--text-soft);
  }
  .divider {
    position: absolute;
    left: 565px;
    top: 934px;
    width: 3px;
    height: 186px;
    background: var(--divider);
  }
  .contact {
    position: absolute;
    left: 596px;
    top: 944px;
    margin: 0;
    padding: 0;
    list-style: none;
    font-family: "Open Sans", sans-serif;
    font-size: 24px;
    color: var(--text-white);
  }
  .contact__item {
    display: flex;
    align-items: flex-start;
    line-height: 32px;
    margin-bottom: 3px;
  }
  .contact__icon {
    width: 28px;
    height: 28px;
    margin: 2px 22px 0 0;
    flex: none;
  }
</style>
</head>
<body>
<main class="canvas">
  <section class="card card--front" aria-label="Card front">
    <div class="brand">
      <span class="brand__dot"></span>
      <span class="brand__name">Halvex Consulting</span>
    </div>
  </section>

  <section class="card card--back" aria-label="Card back">
    <div class="back-mark"></div>
  </section>

  <div class="person">
    <h1 class="person__name">Gareth Pollard</h1>
    <p class="person__role">Unified Communications<br>and Network Architect<br>Design engineer</p>
  </div>

  <div class="divider"></div>

  <ul class="contact">
    <li class="contact__item">
      <svg class="contact__icon" viewBox="0 0 28 28" aria-hidden="true">
        <rect x="2" y="6" width="24" height="16" fill="#fff"/>
        <path d="M2 6 L14 16 L26 6" fill="none" stroke="#1565c8" stroke-width="2"/>
      </svg>
      <span>15520, Harbour View Rd,<br>New Zealand</span>
    </li>
    <li class="contact__item">
      <svg class="contact__icon" viewBox="0 0 28 28" aria-hidden="true">
        <path d="M3 9 Q14 2 25 9 L22 13 L18 11 L18 8 Q14 7 10 8 L10 11 L6 13 Z" fill="#fff"/>
        <rect x="7" y="15" width="14" height="10" rx="2" fill="#fff"/>
      </svg>
      <span>310 555 0142</span>
    </li>
    <li class="contact__item">
      <svg class="contact__icon" viewBox="0 0 28 28" aria-hidden="true">
        <rect x="8" y="2" width="12" height="8" fill="#fff"/>
        <rect x="3" y="11" width="22" height="10" rx="2" fill="#fff"/>
        <rect x="8" y="18" width="12" height="8" fill="#fff" stroke="#1565c8" stroke-width="1.5"/>
      </svg>
      <span>087 555 0199</span>
    </li>
    <li class="contact__item">
      <svg class="contact__icon" viewBox="0 0 28 28" aria-hidden="true">
        <text x="14" y="22" text-anchor="middle" font-family="Open Sans, sans-serif" font-size="24" font-weight="700" fill="#fff">@</text>
      </svg>
      <span>inbox@halvex.com</span>
    </li>
  </ul>
</main>
</body>
</html>
```